PawHush business card

Looking for a fun and cool biz card for a new company with patent pending products. I have products to help and protect dogs hearing. My colors are pantone blue and orange.
Updates

Please add tag line: Protect the ones you love...even your PawHushes!

Target Market(s)

Animal/Dog lovers!

Industry/Entity Type

Retail

Contact Information for Business Card

I'm looking for something simple yet fun with all the info included for biz cards

Colors
0555a3
f78f20

Requirements
Must have
• Logo
Nice to have
• name, website and email
Should not have
• phone number

```html
<!DOCTYPE html>
<html lang="en">
<head>
<meta charset="utf-8">
<title>PawHush business card</title>
<link rel="stylesheet" href="https://fonts.googleapis.com/css2?family=Rubik:wght@500;700&family=Roboto:wght@400;500&display=swap">
<style>
  :root {
    --brand-blue: #273a85;
    --brand-orange: #f1592a;
    --paper: #ffffff;
    --backdrop: #ece8e3;
  }
  * { margin: 0; padding: 0; box-sizing: border-box; }
  html, body {
    width: 1200px;
    height: 800px;
    overflow: hidden;
    background: var(--backdrop);
  }
  .canvas {
    position: relative;
    width: 1200px;
    height: 800px;
  }
  .card {
    position: absolute;
    top: 245px;
    width: 540px;
    height: 310px;
    overflow: hidden;
    box-shadow: 0 6px 18px rgba(0,0,0,0.18);
  }
  /* Back of card */
  .card-back {
    left: 45px;
    background: var(--brand-blue);
  }
  .card-back .side-band {
    position: absolute;
    left: 0; top: 0;
    width: 95px; height: 100%;
    background: var(--brand-orange);
  }
  .card-back .wordmark {
    position: absolute;
    left: 140px;
    top: 100px;
    font-family: "Rubik", sans-serif;
    font-weight: 700;
    font-size: 78px;
    line-height: 1;
    color: var(--brand-orange);
  }
  .tagline {
    position: absolute;
    left: 142px;
    top: 200px;
    width: 380px;
    font-family: "Roboto", sans-serif;
    font-weight: 500;
    font-size: 15px;
    line-height: 1.3;
    color: var(--paper);
    white-space: nowrap;
  }
  /* Front of card */
  .card-front {
    left: 615px;
    background: var(--paper);
  }
  .card-front .wave {
    position: absolute;
    inset: 0;
  }
  .card-front .wordmark {
    position: absolute;
    left: 36px;
    top: 40px;
    font-family: "Rubik", sans-serif;
    font-weight: 700;
    font-size: 84px;
    line-height: 1;
    color: var(--brand-orange);
  }
  .holder-name {
    position: absolute;
    left: 40px;
    top: 212px;
    font-family: "Rubik", sans-serif;
    font-weight: 500;
    font-size: 23px;
    color: var(--brand-orange);
  }
  .contact-list {
    position: absolute;
    left: 315px;
    top: 206px;
    list-style: none;
  }
  .contact-list li {
    display: flex;
    align-items: center;
    gap: 10px;
    height: 32px;
    font-family: "Roboto", sans-serif;
    font-weight: 400;
    font-size: 17px;
    color: var(--paper);
  }
  .contact-list .icon {
    width: 20px;
    height: 20px;
    flex: none;
  }
</style>
</head>
<body>
<main class="canvas">

  <section class="card card-back" aria-label="Card back">
    <div class="side-band"></div>
    <div class="wordmark">PawHush</div>
    <p class="tagline">Protect the ones you love...even your PawHushes!</p>
  </section>

  <section class="card card-front" aria-label="Card front">
    <svg class="wave" viewBox="0 0 540 310" width="540" height="310" aria-hidden="true">
      <path d="M0,185 C150,140 350,150 540,128 L540,310 L0,310 Z" fill="var(--brand-blue)"/>
      <path d="M250,160 C380,150 470,138 540,95 L540,112 C470,150 380,160 250,160 Z" fill="var(--brand-orange)"/>
    </svg>

    <div class="wordmark">PawHush</div>
    <div class="holder-name">Marc Delorme</div>

    <ul class="contact-list">
      <li>
        <svg class="icon" viewBox="0 0 20 20" aria-hidden="true">
          <circle cx="10" cy="10" r="10" fill="var(--brand-orange)"/>
          <rect x="5" y="6.5" width="10" height="7" rx="1" fill="var(--brand-blue)"/>
          <path d="M5.3,7 L10,10.6 L14.7,7" fill="none" stroke="var(--brand-orange)" stroke-width="1"/>
        </svg>
        <span>marc@pawhush.com</span>
      </li>
      <li>
        <svg class="icon" viewBox="0 0 20 20" aria-hidden="true">
          <circle cx="10" cy="10" r="10" fill="var(--brand-orange)"/>
          <g fill="none" stroke="var(--brand-blue)" stroke-width="1.2">
            <circle cx="10" cy="10" r="5"/>
            <ellipse cx="10" cy="10" rx="2.2" ry="5"/>
            <line x1="5" y1="10" x2="15" y2="10"/>
          </g>
        </svg>
        <span>www.pawhush.com</span>
      </li>
    </ul>
  </section>

</main>
</body>
</html>
```